SkyRavelin Unique Gift Certificate

We need a unique, luxury gift certificate created for our online company (SkyRavelin). We are looking for something out of the ordinary, ie. do not want it to look like a 'normal' gift certificate. Please visit our website to gain a feel for our company (skyravelin.com.au). The dimensions are 148x148mm. We need our logo, website details, to, from, description, code, exp date included. The certificate will be printed on wood veneer so watermarks will not work. We want it to be clean and minimalistic.

Industry/Entity Type

It Company

```html
<!DOCTYPE html>
<html lang="en">
<head>
<meta charset="utf-8">
<title>SkyRavelin Gift Certificate</title>
<link rel="stylesheet" href="https://fonts.googleapis.com/css2?family=Open+Sans:wght@400;600&display=swap">
<style>
  :root {
    --wood-light: #93725a;
    --wood-dark: #7a5a43;
    --line: #3b2a1e;
    --teal: #2a7f9a;
    --espresso: #3a2b22;
    --charcoal: #2b2420;
    --stone: #d9d3cc;
    --mist: #e6e6e6;
    --ink-light: #f1ece6;
    --ink-dark: #3a332e;
    --brand: #2a7f9a;
  }
  html, body {
    margin: 0;
    padding: 0;
    overflow: hidden;
    background: #ffffff;
  }
  .certificate {
    position: relative;
    width: 1200px;
    height: 1169px;
    overflow: hidden;
    font-family: "Open Sans", Arial, sans-serif;
  }
  .certificate__honeycomb {
    position: absolute;
    inset: 0;
    width: 1200px;
    height: 1169px;
    display: block;
  }
  .cell {
    stroke: var(--line);
    stroke-width: 2.5;
    vector-effect: non-scaling-stroke;
  }
  .cell--empty { fill: none; }
  .cell--teal { fill: var(--teal); }
  .cell--espresso { fill: var(--espresso); }
  .cell--charcoal { fill: var(--charcoal); }
  .cell--stone { fill: var(--stone); }
  .cell--mist { fill: var(--mist); }

  .field {
    position: absolute;
    margin: 0;
    font-size: 26px;
    line-height: 1;
    font-weight: 400;
  }
  .field--light { color: var(--ink-light); }
  .field--dark { color: var(--ink-dark); }

  .recipient { left: 102px; top: 514px; }
  .sender { left: 102px; top: 564px; }
  .code { left: 562px; top: 758px; }
  .expiry { left: 562px; top: 808px; }
  .website { left: 102px; top: 1034px; font-size: 25px; }

  .description {
    position: absolute;
    left: 470px;
    width: 500px;
    top: 162px;
    margin: 0;
    text-align: center;
    color: var(--ink-light);
    font-size: 23px;
    line-height: 27px;
  }

  .brand {
    position: absolute;
    left: 1030px;
    top: 910px;
    width: 180px;
    display: flex;
    flex-direction: column;
    align-items: center;
  }
  .brand__dot {
    width: 130px;
    height: 130px;
    border-radius: 50%;
    border: 4px solid var(--brand);
    box-sizing: border-box;
  }
  .brand__name {
    margin-top: 16px;
    font-size: 24px;
    font-weight: 600;
    color: var(--brand);
  }
</style>
</head>
<body>
<main class="certificate">
  <svg class="certificate__honeycomb" viewBox="0 0 412 409" preserveAspectRatio="none" xmlns="http://www.w3.org/2000/svg">
    <defs>
      <linearGradient id="woodTone" x1="0" y1="0" x2="1" y2="1">
        <stop offset="0" stop-color="#93725a"/>
        <stop offset="0.5" stop-color="#86664e"/>
        <stop offset="1" stop-color="#7a5a43"/>
      </linearGradient>
    </defs>
    <rect width="412" height="409" fill="url(#woodTone)" role="img" aria-label="Wood veneer grain surface"/>

    <polygon class="cell cell--empty" points="-148,100 -113,25 -5,25 30,100 -5,175 -113,175"/>
    <polygon class="cell cell--empty" points="-148,280 -113,205 -5,205 30,280 -5,355 -113,355"/>

    <polygon class="cell cell--empty" points="5,20 40,-55 148,-55 183,20 148,95 40,95"/>
    <polygon class="cell cell--teal" points="5,188 40,113 148,113 183,188 148,263 40,263"/>
    <polygon class="cell cell--charcoal" points="5,368 40,293 148,293 183,368 148,443 40,443"/>

    <polygon class="cell cell--espresso" points="158,115 195,28 299,28 336,115 299,200 195,200"/>
    <polygon class="cell cell--stone" points="158,280 193,205 301,205 336,280 301,355 193,355"/>
    <polygon class="cell cell--empty" points="158,450 193,375 301,375 336,450 301,525 193,525"/>

    <polygon class="cell cell--empty" points="311,20 346,-55 454,-55 489,20 454,95 346,95"/>
    <polygon class="cell cell--empty" points="311,192 346,117 454,117 489,192 454,267 346,267"/>
    <polygon class="cell cell--mist" points="311,370 346,295 454,295 489,370 454,445 346,445"/>
  </svg>

  <p class="description">
    here you can<br>
    write your gift card<br>
    description. here you<br>
    can write your gift card<br>
    description here you can<br>
    write your gift card description<br>
    here you can write your gift<br>
    card description here you<br>
    can write your gift card<br>
    description can write<br>
    your gift card<br>
    description
  </p>

  <p class="field field--light recipient">to:</p>
  <p class="field field--light sender">from:</p>

  <p class="field field--dark code">code:</p>
  <p class="field field--dark expiry">expiration date:</p>

  <p class="field field--light website">www.skyravelin.com.au</p>

  <div class="brand">
    <span class="brand__dot"></span>
    <span class="brand__name">SkyRavelin</span>
  </div>
</main>
</body>
</html>
```